Company Real Estate Site Needs A Face Lift

I need a new website for the recent company I formed: Voska Real Estate.
You can use my agent website WWW.PALMIROQ.COM to see the style/brand I already have. I will have areas for Searching for homes on IDX, etc.
I really like this site:
http://www.cranfeltmanorhomes.com/
I have attached my logo as well

Industry/Entity Type

Real Estate

Colors
0255a3
ffffff
cee9f5

```html
<!DOCTYPE html>
<html lang="en">
<head>
<meta charset="utf-8">
<title>Voska Real Estate</title>
<link href="https://fonts.googleapis.com/css2?family=Lato:wght@400;700&family=Open+Sans:wght@400;600&display=swap" rel="stylesheet">
<style>
:root{
  --brand-blue:#0255a3;
  --sky:#cee9f5;
  --band-blue:#84c6e4;
  --nav-blue:#8ecbe6;
  --white:#ffffff;
  --ink:#333333;
  --black:#000000;
  --footer-grey:#2a2a2a;
  --hero-top:#7f8884;
  --hero-bottom:#7f9a5c;
  --map-tone:#e2e1dc;
}
*{margin:0;padding:0;box-sizing:border-box}
html,body{width:1200px;height:1142px;overflow:hidden;background:var(--white)}
body{position:relative;font-family:"Lato",sans-serif;color:var(--ink)}
.abs{position:absolute}

/* hero */
.hero-photo{left:0;top:0;width:1200px;height:643px;
  background:linear-gradient(180deg,var(--hero-top) 0%,var(--hero-bottom) 100%)}
.header-shade{left:0;top:0;width:1200px;height:156px}
.logo{left:164px;top:46px;display:flex;align-items:center;gap:10px}
.logo-dot{width:26px;height:26px;border-radius:50%;background:var(--band-blue)}
.logo-name{font-weight:700;font-size:23px;color:var(--white);letter-spacing:1.5px;line-height:1}

.contact-top{left:823px;top:10px;display:flex;align-items:center;gap:6px}
.contact-icon{width:42px;height:42px;border-radius:50%;background:#5db7e0;display:flex;align-items:center;justify-content:center}
.contact-lines{font-size:16px;color:var(--white);line-height:21px}

.follow{left:566px;top:98px;display:flex;align-items:center;gap:8px;font-size:19px;color:var(--white)}
.follow .label{margin-right:8px}
.social{width:27px;height:27px;border-radius:50%;background:var(--white)}

.search-box{left:819px;top:75px;width:239px;height:64px;background:#2e2e2e;padding:7px 11px}
.search-label{font-family:"Open Sans",sans-serif;font-weight:600;font-size:12.5px;color:var(--white);letter-spacing:.3px}
.search-input{margin-top:5px;height:28px;background:var(--white);display:flex;align-items:center;justify-content:space-between;padding:0 6px 0 10px;font-family:"Open Sans",sans-serif;font-size:13px;color:#555}

.nav{left:131px;top:156px;width:938px;height:46px;display:flex;gap:1px;background:#a9d8ec}
.nav a{display:flex;align-items:center;justify-content:center;background:var(--nav-blue);color:#2b3a45;font-weight:700;font-size:12.5px;text-decoration:none;letter-spacing:.2px}
.nav a.active{background:var(--brand-blue);color:var(--white)}

.villa-card{left:692px;top:278px;width:367px;height:229px;background:rgba(30,30,30,.88);padding:34px 37px}
.villa-title{font-size:23px;font-weight:700;color:var(--white)}
.villa-text{margin-top:14px;font-family:"Open Sans",sans-serif;font-size:12.5px;line-height:17px;color:#ddd;width:300px}
.villa-price{margin-top:18px;font-size:24px;font-weight:700;color:var(--white)}
.villa-dot{right:18px;top:15px;width:11px;height:11px;border-radius:50%;background:#ccc}

/* services */
.services{left:0;top:643px;width:1200px;height:212px;background:var(--band-blue)}
.service{top:604px;width:290px;text-align:center}
.service-icon{width:84px;height:84px;border-radius:50%;background:#303030;margin:0 auto;display:flex;align-items:center;justify-content:center}
.service h2{margin-top:11px;font-size:24px;font-weight:700;color:var(--white)}
.service h2 b{color:#2c3e4a}
.service p{width:268px;margin:12px auto 0;font-size:13px;line-height:18px;color:#2f3a40}
.read-more{display:inline-block;margin-top:16px;width:82px;height:27px;line-height:25px;border:1px solid #fff;background:var(--sky);font-size:10px;font-weight:700;color:#333}

.divider{left:160px;top:857px;width:880px;height:2px;background:linear-gradient(90deg,transparent,#ddd,transparent)}
.to-top{left:1050px;top:865px;width:25px;height:25px;border-radius:50%;background:var(--band-blue);border:2px solid #fff;box-shadow:0 0 0 1px #9bb;z-index:5}

.tabs-bar{left:0;top:874px;width:1200px;height:47px;background:repeating-linear-gradient(135deg,#333 0 2px,#3d3d3d 2px 4px)}
.tab{top:874px;height:47px;background:#2e2e2e;color:var(--white);font-weight:700;font-size:15px;display:flex;align-items:center;padding-left:11px;gap:6px;border-left:1px solid #555;border-right:1px solid #555}
.blue-rule{left:0;top:921px;width:1200px;height:2px;background:var(--brand-blue)}

/* footer */
.footer{left:0;top:923px;width:1200px;height:181px;background:var(--black)}
.f-col h3{font-size:15px;font-weight:400;color:var(--white);padding-bottom:11px;border-bottom:1px dashed #555}
.links{display:grid;grid-template-columns:105px 90px;row-gap:13px;margin-top:11px;list-style:none;font-size:12.5px;color:var(--white)}
.links li::before{content:"";display:inline-block;border-left:3px solid #fff;border-top:3px solid transparent;border-bottom:3px solid transparent;margin:0 6px 1px 2px}
.map{left:361px;top:983px;width:178px;height:103px;border:3px solid #ddd;background:var(--map-tone)}
.c-row{display:flex;gap:9px;align-items:flex-start;font-size:12px;line-height:16px;color:var(--white)}
.news-text{font-size:12px;line-height:16px;color:var(--white)}
.news-input{left:787px;top:1023px;width:185px;height:27px;background:var(--white);font-size:13px;color:#666;padding:6px 8px}
.subscribe{left:982px;top:1023px;width:87px;height:27px;background:var(--brand-blue);color:var(--white);font-weight:700;font-size:13px;display:flex;align-items:center;justify-content:center}
.copyright{left:0;top:1104px;width:1200px;height:38px;background:var(--footer-grey);color:var(--white);font-size:13px;display:flex;align-items:center;justify-content:center}
</style>
</head>
<body>

<div class="abs hero-photo" role="img" aria-label="Photo of a two-storey family house with a front garden and lawn"></div>
<svg class="abs header-shade" width="1200" height="156" viewBox="0 0 1200 156">
  <polygon points="0,0 800,0 360,156 0,156" fill="#2f2f2f" fill-opacity=".92"/>
  <polygon points="800,0 1200,0 1200,156 360,156" fill="#222" fill-opacity=".55"/>
</svg>

<div class="abs logo"><span class="logo-dot"></span><span class="logo-name">VOSKA REAL ESTATE</span></div>

<div class="abs contact-top">
  <div class="contact-icon">
    <svg width="20" height="20" viewBox="0 0 20 20"><path d="M4 2l4 3-2 3c1 3 3 5 6 6l2-2 4 3-2 3C8 18 2 12 1 4z" fill="#fff"/></svg>
  </div>
  <div class="contact-lines">+555-014-7720<br>info@voskarealty.com</div>
</div>

<div class="abs follow"><span class="label">Follow Us</span><span class="social"></span><span class="social"></span><span class="social"></span><span class="social"></span></div>

<div class="abs search-box">
  <div class="search-label">Searching for homes on IDX, etc</div>
  <div class="search-input">Search
    <svg width="16" height="16" viewBox="0 0 16 16"><circle cx="6.5" cy="6.5" r="5" fill="none" stroke="#777" stroke-width="2"/><path d="M10 10l5 5" stroke="#777" stroke-width="2.5"/></svg>
  </div>
</div>

<nav class="abs nav">
  <a style="width:111px">HOME</a>
  <a class="active" style="width:126px">COMPANY</a>
  <a style="width:90px">BUY</a>
  <a style="width:89px">SELL</a>
  <a style="width:152px">TESTIMONIALS</a>
  <a style="width:98px">BLOG</a>
  <a style="width:135px">RESOURCES</a>
  <a style="width:130px">CONTACT</a>
</nav>

<div class="abs villa-card">
  <span class="abs villa-dot"></span>
  <div class="villa-title">Villa One</div>
  <div class="villa-text">Lorem ipsum dolor sit amet uer adipicin els diam nonmy nibh euismod t ut laoreet dolore magna erat dolor sit.nibh euismod t ut laoreet d magna erat dolor sit.</div>
  <div class="villa-price">$ 255.25</div>
</div>

<div class="abs services"></div>

<div class="abs service" style="left:127px">
  <div class="service-icon"><svg width="40" height="40" viewBox="0 0 40 40"><circle cx="20" cy="20" r="13" fill="none" stroke="#fff" stroke-width="3"/></svg></div>
  <h2>About <b>Realestate</b></h2>
  <p>Lorem ipsum dolor sit amet uer adipicin elsed diam nonmy nibh euismod t ut laoreet dolore magna&nbsp; erat dolor sit.</p>
  <span class="read-more">READ MORE</span>
</div>
<div class="abs service" style="left:447px">
  <div class="service-icon"><svg width="40" height="40" viewBox="0 0 40 40"><circle cx="20" cy="20" r="15" fill="#fff"/><text x="20" y="24" text-anchor="middle" font-family="Lato,sans-serif" font-weight="700" font-size="11" fill="#303030">BUY</text></svg></div>
  <h2>Buying <b>Services</b></h2>
  <p>Lorem ipsum dolor sit amet uer adipicin elsed diam nonmy nibh euismod t ut laoreet dolore magna&nbsp; erat dolor sit.</p>
  <span class="read-more">READ MORE</span>
</div>
<div class="abs service" style="left:774px">
  <div class="service-icon"><svg width="40" height="40" viewBox="0 0 40 40"><path d="M6 20L20 8l14 12" fill="none" stroke="#fff" stroke-width="3"/><rect x="11" y="19" width="18" height="13" fill="#fff"/></svg></div>
  <h2>Selling <b>Services</b></h2>
  <p>Lorem ipsum dolor sit amet uer adipicin elsed diam nonmy nibh euismod t ut laoreet dolore magna&nbsp; erat dolor sit.</p>
  <span class="read-more">READ MORE</span>
</div>

<div class="abs divider"></div>
<div class="abs tabs-bar"></div>

<div class="abs tab" style="left:131px;width:281px">TESTIMONIALS <svg width="10" height="7" viewBox="0 0 10 7"><path d="M1 1l4 4 4-4" fill="none" stroke="#fff" stroke-width="1.6"/></svg></div>
<div class="abs tab" style="left:460px;width:281px">RECENT POST <svg width="10" height="7" viewBox="0 0 10 7"><path d="M1 1l4 4 4-4" fill="none" stroke="#fff" stroke-width="1.6"/></svg></div>
<div class="abs tab" style="left:788px;width:281px">LATEST NEWS <svg width="10" height="7" viewBox="0 0 10 7"><path d="M1 1l4 4 4-4" fill="none" stroke="#fff" stroke-width="1.6"/></svg></div>
<div class="abs blue-rule"></div>
<div class="abs to-top"><svg width="21" height="21" viewBox="0 0 21 21"><path d="M6 13l4.5-4.5L15 13" fill="none" stroke="#1d4f70" stroke-width="2"/></svg></div>

<footer class="abs footer"></footer>

<div class="abs f-col" style="left:133px;top:941px;width:190px">
  <h3>QUICK LINKS</h3>
  <ul class="links">
    <li>Home</li><li>Testimonials</li>
    <li>Company</li><li>Blog</li>
    <li>Buy</li><li>Resources</li>
    <li>Sell</li><li>Contacts</li>
  </ul>
</div>

<div class="abs f-col" style="left:359px;top:941px;width:400px"><h3>CONTACT US</h3></div>
<div class="abs map" role="img" aria-label="Street map showing the office location"></div>
<div class="abs" style="left:548px;top:983px;width:200px">
  <div class="c-row"><svg width="14" height="18" viewBox="0 0 14 18"><path d="M7 1a6 6 0 0 1 6 6c0 4-6 10-6 10S1 11 1 7a6 6 0 0 1 6-6z" fill="#fff"/><circle cx="7" cy="7" r="2.2" fill="#000"/></svg><span>dolor sit amet uer adipicin elsed diam nonmy nibh adipicin elsed diam nonmy nibh</span></div>
  <div class="c-row" style="margin-top:8px;font-weight:700"><svg width="15" height="11" viewBox="0 0 15 11"><rect width="15" height="11" fill="#fff"/><path d="M0 0l7.5 6L15 0" fill="none" stroke="#000" stroke-width="1.3"/></svg><span>info@voskarealty.com</span></div>
  <div class="c-row" style="margin-top:10px;font-size:18px;line-height:20px"><svg width="12" height="16" viewBox="0 0 12 16" style="margin-top:2px"><rect x="1" y="1" width="10" height="14" rx="1.5" fill="#fff"/><rect x="3" y="3" width="6" height="4" fill="#000"/></svg><span>+555-014-7720</span></div>
</div>

<div class="abs f-col" style="left:787px;top:941px;width:282px">
  <h3>NEWSLETTER SIGNUP</h3>
  <p class="news-text" style="margin-top:12px">dolor sit amet uer adipicin elsed diam nonmy nibh adipicin elsed diam nonmy nibh</p>
</div>
<div class="abs news-input">Email Id:</div>
<div class="abs subscribe">SUBSCRIBE</div>

<div class="abs copyright">© 2014 Voska Real Estate | All Rights Reserved.</div>

</body>
</html>
```